Mindfulness School for Children -- Business Cards

We're looking for business cards for our school directors and owners. We're a mindfulness school for children called little compass. Attached are our logos/icons.

```html
<!DOCTYPE html>
<html lang="en">
<head>
<meta charset="utf-8">
<title>little compass — Business Cards</title>
<link href="https://fonts.googleapis.com/css2?family=Roboto:wght@400;500&display=swap" rel="stylesheet">
<style>
  :root {
    --backdrop: #cdcdcd;
    --card-teal: #489bae;
    --mark-tint: #68b8d0;
    --card-ink: #e6f1f4;
    --card-paper: #e2e2e6;
    --brand-teal: #4a9db0;
  }
  * { margin: 0; padding: 0; box-sizing: border-box; }
  html, body {
    width: 1200px; height: 1101px; overflow: hidden;
    background: var(--backdrop);
    font-family: "Roboto", Arial, sans-serif;
  }
  .stage { position: relative; width: 1200px; height: 1101px; }
  .card {
    position: absolute; top: 266px;
    width: 302px; height: 533px;
  }
  .card--front { left: 246px; background: var(--card-teal); color: var(--card-ink); }
  .card--back { left: 641px; background: var(--card-paper); }

  .holder { position: absolute; left: 35px; top: 50px; }
  .holder__name { font-size: 22px; font-weight: 500; letter-spacing: 0.2px; line-height: 1.2; }
  .holder__role { font-size: 14px; font-weight: 400; margin-top: 2px; }

  .brand-emblem {
    position: absolute; left: 51px; top: 126px;
    width: 200px; height: 200px;
  }
  .brand-emblem__disc {
    position: absolute; inset: 0; border-radius: 50%;
    background: var(--mark-tint); opacity: 0.55;
  }
  .brand-emblem__name {
    position: absolute; inset: 0; display: flex;
    align-items: center; justify-content: center;
    font-size: 22px; font-weight: 400; color: var(--card-teal);
  }

  .contact-icons { position: absolute; left: 35px; top: 352px; display: flex; gap: 11px; }
  .contact-icons svg { width: 21px; height: 21px; display: block; }

  .contact { position: absolute; left: 35px; top: 382px; font-size: 14.5px; line-height: 19.5px; }
  .address { position: absolute; left: 35px; top: 455px; font-size: 14.5px; line-height: 19.5px; }

  .wordmark {
    position: absolute; left: 50%; top: 50%;
    transform: translate(-50%, -50%) rotate(-90deg);
    display: flex; align-items: center; gap: 10px;
    white-space: nowrap;
  }
  .wordmark__dot { width: 22px; height: 22px; border-radius: 50%; background: var(--brand-teal); }
  .wordmark__name { font-size: 44px; font-weight: 400; color: var(--brand-teal); letter-spacing: 0.5px; }
</style>
</head>
<body>
<main class="stage">
  <section class="card card--front">
    <div class="holder">
      <h1 class="holder__name">MARCUS LANE</h1>
      <p class="holder__role">General Manager</p>
    </div>

    <div class="brand-emblem">
      <div class="brand-emblem__disc"></div>
      <div class="brand-emblem__name">little compass</div>
    </div>

    <div class="contact-icons">
      <svg viewBox="0 0 20 20" aria-label="phone"><circle cx="10" cy="10" r="10" fill="var(--card-ink)"/><path d="M6.3 5.2l1.8-.4 1.1 2.6-1.2 1a7 7 0 0 0 3.6 3.6l1-1.2 2.6 1.1-.4 1.8c-4.6.4-8.9-3.9-8.5-8.5z" fill="var(--card-teal)"/></svg>
      <svg viewBox="0 0 20 20" aria-label="email"><circle cx="10" cy="10" r="10" fill="var(--card-ink)"/><rect x="5" y="6.5" width="10" height="7" fill="none" stroke="var(--card-teal)" stroke-width="1.2"/><path d="M5 6.5l5 4 5-4M5 13.5l3.6-3.4M15 13.5l-3.6-3.4" fill="none" stroke="var(--card-teal)" stroke-width="1"/></svg>
      <svg viewBox="0 0 20 20" aria-label="website"><circle cx="10" cy="10" r="10" fill="var(--card-ink)"/><g fill="none" stroke="var(--card-teal)" stroke-width="1"><circle cx="10" cy="10" r="5.5"/><ellipse cx="10" cy="10" rx="2.4" ry="5.5"/><path d="M4.5 10h11M5.3 7.2h9.4M5.3 12.8h9.4"/></g></svg>
    </div>

    <p class="contact">(555) 218-4470<br>marcus@littlecompass.com<br>www.littlecompass.com</p>
    <p class="address">418 W. Harbor Lane<br>Maple Cove, CA 90210</p>
  </section>

  <section class="card card--back">
    <div class="wordmark">
      <span class="wordmark__dot"></span>
      <span class="wordmark__name">little compass</span>
    </div>
  </section>
</main>
</body>
</html>
```